Design the Mobile Version of Existing Web Based Health Platform

Loomcrest is a social business enterprise that focus on public health by applying innovative healthcare services and consumer internet technology. Loomcrest offers a personalized platform of health promotion and disease prevention that puts the individual back in control of his life.

Loomcrest is looking for a Mobile Web UX/Visual Design professional to create a mobile version of Loomcrest website platform for iPhone, iPad/tablet and Android.

Contestants must to check www.loomcrest-demo.com.br to have a better understanding of Loomcrest Platform by creating an account (it's in portuguese, but anyone can get the general idea).

The mobile version of Loomcrest should have very similar functionality and user flows. This job is not to reengineer or re-imagine Loomcrest. It is just to reformat the existing functionality so it works well on mobile devices.

This description below is to help you to understand the core features of the platform (check the attachments to see the new web design of each one):

- Personally Controlled Health Record - PCHR enables an individual to own and manage a complete, secure, digital copy of her health and wellness information.
- Health Risk Assessments - is a process to estimate the nature and probability of adverse health effects, based on personal and family historical data, behavior and environment.
- Simulation of future health - "what if analysis" that emphasizes health education and behavior change.
- Step Quests - a program that gives you the opportunity to the participant to advance his personal well-being by doing simple Step Quests
- Health Alerts and Recommendations and Missing Data - Recommendations based on Wellbeing Bureau Guidelines and Federal Wellness Review Panel (FWRP), plus notifications to update outdated information.

The deliverable for this project is a psd file with a designed mobile version of Loomcrest.

A new design of the web platform is under construction. You can also check it looking at the files attached.

Target Market(s)

people 25-40 years old, 60% female, socially engaged

Industry/Entity Type

Healthcare

Requirements
Must have
• iPhone, iPad and Android version

Design must cover all current functionalities available on the web version (please, ensure you understand all features by creating an account at www.loomcrest-demo.com.br)

- Login/Sign up
- Welcome (first assessment)
- Add to Personal Controlled Health Record (PCHR)
- Update/Remove PCHR
- List PCHR
- Riskgrid (risk assessmen results)
- Simulation
- Alerts
- Missing data
- Recommendations
- StepQuest
- Badges
- Configurations

It's important to check the attachments to see how the web platform design is evolving.

```html
<!DOCTYPE html>
<html lang="en">
<head>
<meta charset="utf-8">
<title>Loomcrest – Badges</title>
<link href="https://fonts.googleapis.com/css2?family=Arimo:wght@400;700&display=swap" rel="stylesheet">
<style>
:root{
  --orange:#f7883a;
  --orange-light:#f9a262;
  --green:#8cc63f;
  --grey-dark:#5a5a5a;
  --grey-icon:#8e9094;
  --line:#c9c9c9;
  --bg:#f6f6f4;
  --bar:#f3f3f3;
  --white:#ffffff;
}
*{box-sizing:border-box;margin:0;padding:0}
html,body{width:799px;height:1200px;overflow:hidden}
body{background:var(--bg);font-family:"Arimo",Arial,sans-serif;position:relative}
.app-header{position:absolute;left:0;top:0;width:799px;height:90px;background:linear-gradient(#ffffff,#ececec);border-bottom:1px solid var(--line)}
.avatar{position:absolute;left:10px;top:10px;width:77px;height:75px;background:linear-gradient(160deg,#c98a6a,#5e6a78 60%,#2e3a44)}
.avatar-toggle{position:absolute;left:96px;top:40px}
.divider{position:absolute;top:0;width:1px;height:90px;background:var(--line)}
.brand{position:absolute;left:250px;top:20px;display:flex;align-items:center;gap:12px}
.brand-mark{width:48px;height:48px;background:var(--orange);border-radius:8px}
.brand-name{font-size:44px;font-weight:700;color:var(--green);letter-spacing:-1px;line-height:1}
.menu-button{position:absolute;left:735px;top:27px}
.record-bar{position:absolute;left:0;top:90px;width:799px;height:72px;background:linear-gradient(var(--orange-light),var(--orange))}
.record-icon{position:absolute;left:71px;top:16px}
.record-input{position:absolute;left:120px;top:17px;width:459px;height:42px;background:var(--white);border:1px solid #e0e0e0;font-size:18px;font-weight:700;color:#b9b9b9;padding:10px 14px}
.partner{position:absolute;left:606px;top:22px;display:flex;align-items:center;gap:7px}
.partner-dot{width:26px;height:26px;border-radius:50%;background:#1f3a6b}
.partner-name{font-size:15px;font-weight:700;color:#1f3a6b;line-height:15px;width:100px}
.badge{position:absolute;width:260px;text-align:center}
.badge.locked{opacity:.3}
.badge-frame{margin:0 auto;width:170px;height:150px;border:7px solid var(--orange);border-radius:10px 30px 10px 30px;display:flex;align-items:center;justify-content:center}
.badge-label{margin-top:16px;font-size:21px;font-weight:700;color:var(--green);white-space:nowrap}
.tab-bar{position:absolute;left:0;top:1118px;width:799px;height:82px;background:linear-gradient(#fafafa,#e9e9e9);border-top:1px solid var(--line)}
.tab{position:absolute;top:14px}
.tab-count{position:absolute;left:22px;top:30px;width:26px;height:26px;border-radius:50%;background:var(--orange);color:var(--white);font-size:13px;font-weight:700;text-align:center;line-height:26px;border:2px solid var(--white)}
</style>
</head>
<body>
<header class="app-header">
  <div class="avatar" role="img" aria-label="User profile photo"></div>
  <svg class="avatar-toggle" width="22" height="14" viewBox="0 0 22 14"><path d="M2 2l9 9 9-9" fill="none" stroke="var(--grey-dark)" stroke-width="4"/></svg>
  <div class="divider" style="left:125px"></div>
  <div class="brand"><span class="brand-mark"></span><span class="brand-name">Loomcrest</span></div>
  <div class="divider" style="left:710px"></div>
  <svg class="menu-button" width="44" height="38" viewBox="0 0 44 38"><g fill="var(--grey-dark)"><rect width="44" height="9" rx="4.5"/><rect y="14" width="44" height="9" rx="4.5"/><rect y="28" width="44" height="9" rx="4.5"/></g></svg>
</header>

<section class="record-bar">
  <svg class="record-icon" width="30" height="40" viewBox="0 0 30 40"><rect x="1" y="4" width="28" height="35" rx="3" fill="#fde2c8" stroke="var(--white)" stroke-width="2"/><rect x="9" y="1" width="12" height="7" rx="2" fill="var(--white)"/><g fill="var(--orange)"><rect x="6" y="14" width="3" height="3"/><rect x="11" y="14" width="13" height="3"/><rect x="6" y="21" width="3" height="3"/><rect x="11" y="21" width="13" height="3"/><rect x="6" y="28" width="3" height="3"/><rect x="11" y="28" width="13" height="3"/></g></svg>
  <div class="record-input">Add a new record</div>
  <div class="partner"><span class="partner-dot"></span><span class="partner-name">Halvern Pharma</span></div>
</section>

<svg width="0" height="0" style="position:absolute">
  <defs>
    <g id="trophy">
      <path d="M22 6h76v24c0 30-16 46-38 50-22-4-38-20-38-50z" fill="var(--green)"/>
      <path d="M22 14H6c0 22 10 34 26 36M98 14h16c0 22-10 34-26 36" fill="none" stroke="var(--green)" stroke-width="7"/>
      <rect x="54" y="78" width="12" height="14" fill="var(--green)"/>
      <rect x="44" y="92" width="32" height="8" fill="var(--green)"/>
      <rect x="36" y="100" width="48" height="9" fill="var(--green)"/>
      <path d="M60 22l5 11 12 1-9 8 3 12-11-6-11 6 3-12-9-8 12-1z" fill="var(--white)"/>
    </g>
  </defs>
</svg>

<main class="badges">
  <div class="badge" style="left:82px;top:221px"><div class="badge-frame"><svg width="120" height="110"><use href="#trophy"/></svg></div><p class="badge-label">Information basic</p></div>
  <div class="badge locked" style="left:446px;top:221px"><div class="badge-frame"><svg width="120" height="110"><use href="#trophy"/></svg></div><p class="badge-label">10 Desafios do dai</p></div>
  <div class="badge locked" style="left:82px;top:446px"><div class="badge-frame"><svg width="120" height="110"><use href="#trophy"/></svg></div><p class="badge-label">10 Desafios do dai</p></div>
  <div class="badge locked" style="left:446px;top:446px"><div class="badge-frame"><svg width="120" height="110"><use href="#trophy"/></svg></div><p class="badge-label">Information Afancadas</p></div>
  <div class="badge locked" style="left:82px;top:675px"><div class="badge-frame"><svg width="120" height="110"><use href="#trophy"/></svg></div><p class="badge-label">10 Desafios do dai</p></div>
  <div class="badge locked" style="left:446px;top:675px"><div class="badge-frame"><svg width="120" height="110"><use href="#trophy"/></svg></div><p class="badge-label">Information Afancadas</p></div>
  <div class="badge locked" style="left:82px;top:897px"><div class="badge-frame"><svg width="120" height="110"><use href="#trophy"/></svg></div><p class="badge-label">10 Desafios do dai</p></div>
  <div class="badge locked" style="left:446px;top:897px"><div class="badge-frame"><svg width="120" height="110"><use href="#trophy"/></svg></div><p class="badge-label">Information Afancadas</p></div>
</main>

<nav class="tab-bar">
  <svg class="tab" style="left:74px" width="48" height="46" viewBox="0 0 48 46"><g fill="var(--grey-icon)"><rect x="0" y="4" width="13" height="12"/><rect x="16" y="4" width="13" height="12"/><rect x="33" y="0" width="14" height="14" transform="rotate(10 40 7)"/><rect x="0" y="19" width="13" height="12"/><rect x="16" y="19" width="13" height="12"/><rect x="32" y="18" width="13" height="12"/><rect x="0" y="34" width="13" height="12"/><rect x="16" y="34" width="13" height="12"/></g></svg>
  <div class="tab" style="left:220px">
    <svg width="48" height="44" viewBox="0 0 48 44"><path d="M24 2L46 42H2z" fill="var(--grey-icon)" stroke="var(--grey-icon)" stroke-width="3" stroke-linejoin="round"/><rect x="21" y="14" width="6" height="15" fill="var(--white)"/><rect x="21" y="32" width="6" height="6" fill="var(--white)"/></svg>
    <span class="tab-count">15</span>
  </div>
  <svg class="tab" style="left:373px" width="48" height="46" viewBox="0 0 48 46"><path d="M4 18L24 4l20 14v26H4z" fill="var(--grey-icon)"/><rect x="11" y="10" width="26" height="22" fill="var(--white)"/><g fill="var(--grey-icon)"><rect x="15" y="14" width="18" height="3"/><rect x="15" y="20" width="18" height="3"/><rect x="15" y="26" width="12" height="3"/></g><path d="M4 20l20 14 20-14" fill="var(--grey-icon)" stroke="var(--white)" stroke-width="2"/></svg>
  <svg class="tab" style="left:518px" width="58" height="46" viewBox="0 0 58 46"><path d="M29 2c15 0 27 8 27 19s-12 19-27 19c-4 0-7 0-10-1L8 45l3-10C5 31 2 26 2 21 2 10 14 2 29 2z" fill="var(--grey-icon)"/><g fill="var(--white)"><circle cx="18" cy="21" r="4"/><circle cx="29" cy="21" r="4"/><circle cx="40" cy="21" r="4"/></g></svg>
  <svg class="tab" style="left:678px" width="44" height="44" viewBox="0 0 44 44"><circle cx="22" cy="22" r="21" fill="var(--grey-icon)"/><path d="M15 17c0-5 3-8 7-8s7 3 7 7c0 5-6 5-6 11" fill="none" stroke="var(--white)" stroke-width="5"/><rect x="20" y="31" width="6" height="5" fill="var(--white)"/></svg>
</nav>
</body>
</html>
```